Need Business Cards for my Business

email address: rkpmarlowhollowworks@vendrimail.com
web address: rkpmarlowhollowworks.net
Slogan: We offer various QVN licenses
Rowland K. Pemberly
Please stick with colors of Company Logo
would like the card to be more of the color example of the logo.
If you need PDF copy of logo email me at the above account.
Creative control rests with you.

Industry/Entity Type

Business

Contact Information for Business Card

I am a minimalist, but would like something to pop and stand out amongst other cards, make it memorable.

Font styles to use
Serif
Decorative
Script

```html
<!DOCTYPE html>
<html lang="en">
<head>
<meta charset="utf-8">
<title>RKP Marlow Hollow Works – Business Card</title>
<link rel="stylesheet" href="https://fonts.googleapis.com/css2?family=Open+Sans:wght@400;600;700&display=swap">
<style>
  :root {
    --backdrop: #dcdbdc;
    --card: #ffffff;
    --brand-red: #e3242b;
    --brand-red-deep: #c21f2e;
    --brand-navy: #1d3d6e;
    --ink: #1f2a44;
  }
  * { box-sizing: border-box; margin: 0; padding: 0; }
  html, body {
    width: 1200px; height: 1000px; overflow: hidden;
    background: var(--backdrop);
    font-family: "Open Sans", Arial, sans-serif;
  }
  .canvas { position: relative; width: 1200px; height: 1000px; }
  .card { position: absolute; background: var(--card); }
  .card--front { left: 305px; top: 24px; width: 592px; height: 338px; }
  .card--back { left: 456px; top: 384px; width: 338px; height: 592px; }

  .brand {
    position: absolute; display: flex; align-items: center; gap: 10px;
    color: var(--brand-navy); font-weight: 700; white-space: nowrap;
  }
  .brand__dot { border-radius: 50%; background: var(--brand-red); flex: none; }
  .card--front .brand { left: 0; right: 0; top: 176px; justify-content: center; font-size: 26px; }
  .card--front .brand__dot { width: 22px; height: 22px; }
  .card--back .brand { left: 0; right: 0; top: 176px; justify-content: center; font-size: 17px; }
  .card--back .brand__dot { width: 15px; height: 15px; }

  .slogan-band {
    position: absolute; left: 0; right: 0; top: 302px; height: 26px;
    background: linear-gradient(90deg, var(--brand-red), var(--brand-red-deep));
    color: #fff; font-size: 15px; text-align: center; line-height: 26px;
    text-transform: uppercase; letter-spacing: 0.2px;
  }

  .contact { position: absolute; left: 50px; right: 0; top: 355px; }
  .contact__name { color: var(--brand-red); font-size: 15px; line-height: 20px; }
  .contact__rule { height: 2px; background: var(--brand-red); margin: 1px 0 4px -3px; }
  .contact__title { color: var(--ink); font-size: 13px; font-weight: 600; }
  .contact__details { list-style: none; margin-top: 24px; color: var(--ink); font-size: 14px; line-height: 19px; }
</style>
</head>
<body>
<main class="canvas">
  <section class="card card--front" aria-label="Card front">
    <div class="brand"><span class="brand__dot"></span>RKP Marlow Hollow Works</div>
    <div class="slogan-band">We offer various QVN licenses</div>
  </section>

  <section class="card card--back" aria-label="Card back">
    <div class="brand"><span class="brand__dot"></span>RKP Marlow Hollow Works</div>
    <div class="contact">
      <p class="contact__name">Rowland K. Pemberly</p>
      <div class="contact__rule"></div>
      <p class="contact__title">Director</p>
      <ul class="contact__details">
        <li>415-555-0148</li>
        <li>rkpmarlowhollowworks@vendrimail.com</li>
        <li>rkpmarlowhollowworks.net</li>
      </ul>
    </div>
  </section>
</main>
</body>
</html>
```